Official personalized stationery with official coat of arms

I am looking for custom stationery design such as US letter size (8.5 X 11 or 21.6cm X 27.9cm), email signature (email) and envelope for US letter size (standard envelope no. 10 or 10.5cm X 24.5cm). Inspired by my personal coat of arms and my postal address:

4186 rue des Saules
Levis, Quebec, G7K 3M2
Canada

Ideally a discreet design based on the coat of arms of Lucien Morvand but inspired by my mother's original coat of arms.

Something golden and translucent, simple but tasteful, without overemphasizing the green color. The coat of arms should have green, but not the entire structure of the stationery.

I am also looking for a small official thank you card in half letter size.

The design must be with the Lucien Morvand coat of arms and not the full coat of arms

Target Market(s)

For official communication

Industry/Entity Type

Communication officiel et parlementaire

Font styles to use
Other font styles liked:
• J’aime bien l’écriture comme le logo de la maison Velloze la police pour écrire le nom Velloze

Requirements
Must have
• Simplicity and use the Lucien Morvand coat of arms and not the full coat of arms
Nice to have
• Official and royal appearance as it is an official heraldic title of the British crown
Should not have
• Email and website

```html
<!DOCTYPE html>
<html lang="fr">
<head>
<meta charset="utf-8">
<title>Papeterie officielle – Lucien Morvand</title>
<link href="https://fonts.googleapis.com/css2?family=Lora:wght@400;700&display=swap" rel="stylesheet">
<style>
  :root {
    --backdrop: #e2e3e4;
    --paper: #ffffff;
    --edge: #d2d3d5;
    --green: #0f5714;
    --gold: #c1923a;
    --ink: #1b1b1b;
    --serif: "Lora", Georgia, serif;
  }
  html, body { margin: 0; padding: 0; }
  body {
    width: 1200px; height: 900px; overflow: hidden;
    background: var(--backdrop);
    font-family: var(--serif);
    color: var(--ink);
    position: relative;
  }
  p { margin: 0; }
  .sheet {
    position: absolute;
    background: var(--paper);
    border: 1px solid var(--edge);
    box-sizing: border-box;
    overflow: hidden;
  }
  .sheet svg.swoosh { position: absolute; left: 0; top: 0; }
  .arms-name {
    position: absolute;
    display: flex; align-items: center; justify-content: center;
    text-align: center;
    color: var(--green);
    font-weight: 700;
    line-height: 1.2;
  }
  .rule { position: absolute; height: 2px; background: var(--green); }
  .address { position: absolute; white-space: nowrap; }

  /* Letterhead */
  .letterhead { left: 57px; top: 102px; width: 534px; height: 691px; }
  .letterhead .arms-name { left: 91px; top: 23px; width: 97px; height: 152px; font-size: 15px; }
  .letterhead .rule { left: 74px; top: 657px; width: 387px; }
  .letterhead .address { left: 0; right: 0; top: 668px; text-align: center; font-size: 9.5px; }

  /* Envelope front */
  .envelope-front { left: 671px; top: 103px; width: 471px; height: 236px; }
  .envelope-front .arms-name { left: 31px; top: 23px; width: 70px; height: 104px; font-size: 11px; }
  .envelope-front .faint-name {
    position: absolute; left: 319px; top: 20px; width: 148px; height: 180px;
    display: flex; align-items: center; justify-content: center; text-align: center;
    color: var(--green); opacity: 0.07; font-weight: 700; font-size: 30px; line-height: 1.15;
  }
  .envelope-front .rule { left: 31px; top: 204px; width: 409px; height: 1.5px; }
  .envelope-front .address { left: 31px; top: 213px; font-size: 7.5px; }

  /* Envelope back */
  .envelope-back { left: 671px; top: 370px; width: 471px; height: 236px; }
  .envelope-back .flap {
    position: absolute; left: 7px; right: 7px; top: -1px; height: 66px;
    border: 1px solid var(--edge); border-top: none;
    border-radius: 0 0 8px 8px;
  }
  .envelope-back .arms-name { left: 200px; top: 10px; width: 70px; height: 40px; font-size: 6.5px; }

  /* Business card */
  .card { left: 670px; top: 648px; width: 266px; height: 134px; }
  .card .arms-name { left: 18px; top: 24px; width: 50px; height: 72px; font-size: 7.5px; }
  .card .holder { position: absolute; left: 152px; top: 34px; }
  .card .holder-name { font-size: 8.5px; font-weight: 700; }
  .card .holder-role { font-size: 5.5px; }
  .card .holder-rule { width: 23px; height: 1px; background: var(--green); margin-top: 2px; }
  .card .contacts { position: absolute; left: 154px; top: 63px; list-style: none; margin: 0; padding: 0; }
  .card .contacts li { display: flex; align-items: center; gap: 4px; font-size: 5.5px; height: 8.7px; white-space: nowrap; }
  .card .contacts svg { width: 5px; height: 5px; fill: var(--green); }
  .card .address { left: 79px; top: 116px; font-size: 5.5px; }
</style>
</head>
<body>

<section class="sheet letterhead" aria-label="Papier à en-tête">
  <svg class="swoosh" width="534" height="240" viewBox="0 0 534 240" aria-hidden="true">
    <path fill="var(--gold)" d="M277,0 C340,60 340,200 42,230 C280,218 400,130 377,0 Z"/>
    <path fill="var(--green)" d="M277,0 C340,60 340,200 42,230 C300,215 375,120 353,0 Z"/>
  </svg>
  <div class="arms-name">Lucien<br>Morvand</div>
  <div class="rule"></div>
  <p class="address">4186 rue des Saules Levis, Quebec, G7K 3M2, Canada</p>
</section>

<section class="sheet envelope-front" aria-label="Enveloppe, recto">
  <svg class="swoosh" width="471" height="170" viewBox="0 0 471 170" aria-hidden="true">
    <path fill="var(--gold)" d="M141,0 C200,40 200,140 36,155 C180,148 260,90 235,0 Z"/>
    <path fill="var(--green)" d="M141,0 C200,40 200,140 36,155 C190,145 240,80 216,0 Z"/>
  </svg>
  <div class="arms-name">Lucien<br>Morvand</div>
  <div class="faint-name">Lucien<br>Morvand</div>
  <div class="rule"></div>
  <p class="address">4186 rue des Saules Levis, Quebec, G7K 3M2, Canada</p>
</section>

<section class="sheet envelope-back" aria-label="Enveloppe, verso">
  <div class="flap"></div>
  <div class="arms-name">Lucien<br>Morvand</div>
</section>

<section class="sheet card" aria-label="Carte de visite">
  <svg class="swoosh" width="266" height="134" viewBox="0 0 266 134" aria-hidden="true">
    <path fill="var(--gold)" d="M63,0 C110,30 110,110 13,133 C110,115 150,70 140,0 Z"/>
    <path fill="var(--green)" d="M63,0 C110,30 110,110 13,133 C110,112 135,65 123,0 Z"/>
  </svg>
  <div class="arms-name">Lucien<br>Morvand</div>
  <div class="holder">
    <p class="holder-name">Émile Tardif</p>
    <p class="holder-role">Owner</p>
    <div class="holder-rule"></div>
  </div>
  <ul class="contacts">
    <li><svg viewBox="0 0 10 10" aria-hidden="true"><path d="M3,0 H7 V10 H3 Z M4,1 V8 H6 V1 Z"/></svg>418-555-0147</li>
    <li><svg viewBox="0 0 10 10" aria-hidden="true"><path d="M0,4 Q5,0 10,4 L8,5 L7,3.5 H3 L2,5 Z M2,6 H8 V10 H2 Z"/></svg>418-555-0147</li>
  </ul>
  <p class="address">4186 rue des Saules Levis, Quebec, G7K 3M2, Canada</p>
</section>

</body>
</html>
```